Book Cover for Notes on the Quiet River's Far Lamps

I need a book cover for a 6 x 9 paperback titled Notes on the Quiet River's Far Lamps Gathered by Sailors and Weavers Resting in the Valley beyond the Northern Valley. It has to do with consciousness, the mind, incarnation onto Earth, leaving Earth, and the life in the life after this life. I have an idea I'm providing with this description, but I am open to anything that would be striking and stimulating, whether with a book or not. I am the author, T. Warren Blakely. I've added another background idea to see if anyone can do something with it and I've increased the budget.

```html
<!DOCTYPE html>
<html lang="en">
<head>
<meta charset="utf-8">
<title>Notes on the Quiet River's Far Lamps — Book Cover</title>
<link rel="stylesheet" href="https://fonts.googleapis.com/css2?family=Exo+2:wght@500;600&family=Roboto+Condensed:wght@700&display=swap">
<style>
  :root {
    --backdrop: #7d7d7f;
    --space-deep: #121a4a;
    --space-mid: #2a3378;
    --nebula-violet: #5a3f78;
    --nebula-rose: #8a5a70;
    --sun-glow: #ffd98a;
    --sun-core: #fff6dc;
    --cloud-light: #e7ecf4;
    --cloud-shadow: #8d97b3;
    --ray-blue: rgba(110, 170, 230, 0.35);
    --title-white: #f7f7fa;
    --author-ink: #0d0d12;
  }
  * { box-sizing: border-box; margin: 0; padding: 0; }
  html, body {
    width: 1200px;
    height: 1200px;
    overflow: hidden;
    background: var(--backdrop);
  }
  .canvas {
    position: relative;
    width: 1200px;
    height: 1200px;
    display: flex;
    align-items: center;
    justify-content: center;
  }
  .book-cover {
    position: relative;
    width: 720px;
    height: 1080px;
    overflow: hidden;
    box-shadow: 0 6px 24px rgba(0, 0, 0, 0.35);
  }
  .cover-art {
    position: absolute;
    inset: 0;
    background:
      radial-gradient(ellipse 38% 7% at 50% 83%, var(--sun-core) 0%, var(--sun-glow) 35%, rgba(255, 190, 110, 0) 100%),
      radial-gradient(ellipse 70% 18% at 50% 82%, rgba(255, 170, 90, 0.55) 0%, rgba(255, 150, 90, 0) 100%),
      linear-gradient(180deg,
        rgba(0, 0, 0, 0) 0%, rgba(0, 0, 0, 0) 83%,
        var(--cloud-light) 85%, var(--cloud-shadow) 90%,
        var(--cloud-light) 94%, var(--cloud-shadow) 100%),
      radial-gradient(ellipse 30% 45% at 50% 0%, var(--ray-blue) 0%, rgba(110, 170, 230, 0) 100%),
      linear-gradient(180deg,
        var(--space-deep) 0%, var(--space-mid) 30%,
        var(--nebula-violet) 58%, var(--nebula-rose) 74%,
        #c48a6a 82%, var(--cloud-light) 85%);
  }
  .cover-text {
    position: absolute;
    inset: 0;
    padding: 0 60px;
  }
  .title {
    position: absolute;
    top: 300px;
    left: 64px;
    font-family: "Exo 2", sans-serif;
    font-weight: 600;
    font-size: 80px;
    line-height: 102px;
    letter-spacing: 0.07em;
    text-transform: uppercase;
    color: var(--title-white);
  }
  .title-line { display: block; }
  .subtitle {
    position: absolute;
    top: 735px;
    left: 66px;
    width: 600px;
    font-family: "Exo 2", sans-serif;
    font-weight: 500;
    font-size: 27px;
    line-height: 34px;
    color: var(--title-white);
  }
  .author {
    position: absolute;
    top: 950px;
    left: 0;
    width: 100%;
    text-align: center;
    font-family: "Roboto Condensed", sans-serif;
    font-weight: 700;
    font-size: 62px;
    letter-spacing: -0.01em;
    color: var(--author-ink);
  }
</style>
</head>
<body>
  <main class="canvas">
    <section class="book-cover">
      <div class="cover-art" role="img" aria-label="Starry space scene with blue light rays, a figure in white floating weightless above, and a sunrise glowing over the curve of a cloud-covered Earth"></div>
      <div class="cover-text">
        <h1 class="title">
          <span class="title-line">Notes on</span>
          <span class="title-line">the Quiet</span>
          <span class="title-line">River's Far</span>
          <span class="title-line">Lamps</span>
        </h1>
        <p class="subtitle">Gathered by Sailors and Weavers Resting in the Valley beyond the Northern Valley</p>
        <p class="author">T. Warren Blakely</p>
      </div>
    </section>
  </main>
</body>
</html>
```